Wedding and event Photography company.

We need a business card design for a photography company based in Singapore named TamKeza. Our core service offering is wedding photojournalism. We would like to see minimalistic designs that use the colour white. The final design should communicate a sense of ease and reliability.

The attached are a couple of visual reference which i found over the web, i hope it will helps.

Project Brief Update (14th July 2014):
- Please refrain from using any images from the website for the design. The laws and regulations over here does not allow me to distribute my client's images. Thanks!

Target Market(s)

Young and middle aged adults aged 24 - 38. With money to spend =D

Industry/Entity Type

Business

Contact Information for Business Card

Name: Dev Lunor
Designation: Head Photographer
Mobile: +65 81749026
Email: jun@tamkeza.example
Website: www.tamkeza.example

Font styles to use
Other font styles liked:
• Baskerville URW

Colors

Designer to choose colors to be used in the design.

Requirements
Must have
• Must include:
• - The brand TamKeza
• - The logo attached
• - Please help to place the brand TamKeza with the logo according to your preferences.
• - Services
• - Wedding Photography
• - Portraiture
• - Photojournalism
Nice to have
• Looking forward to an elegant and simple design. Please see attached examples!
• Please use Serif Fonts
Should not have
• Please refrain from using dark tones for the majority of the design.
• Please refrain from letterpress and embossing.

```html
<!DOCTYPE html>
<html lang="en">
<head>
<meta charset="utf-8">
<title>TamKeza — Business Card</title>
<link rel="stylesheet" href="https://fonts.googleapis.com/css2?family=Libre+Baskerville:wght@400;700&family=Lato:wght@300;400&display=swap">
<style>
  :root {
    --backdrop: #2e2e2e;
    --card: #ffffff;
    --ink: #111111;
    --muted: #8a8a8a;
    --text: #2a2a2a;
  }
  * { box-sizing: border-box; margin: 0; padding: 0; }
  html, body {
    width: 1200px;
    height: 852px;
    overflow: hidden;
    background: var(--backdrop);
  }
  .stage {
    position: relative;
    width: 1200px;
    height: 852px;
  }
  .card {
    position: absolute;
    left: 320px;
    width: 560px;
    height: 320px;
    background: var(--card);
    overflow: hidden;
  }
  .card--front { top: 86px; }
  .card--back { top: 446px; }

  .rule {
    position: absolute;
    left: 0;
    right: 0;
    background: var(--ink);
  }
  .rule--thin { height: 3px; }
  .rule--thick { height: 8px; }

  /* front */
  .card--front .rule--top { top: 10px; }
  .card--front .rule--bottom-thick { bottom: 26px; }
  .card--front .rule--bottom-thin { bottom: 8px; }

  .identity {
    position: absolute;
    top: 50px;
    left: 0;
    right: 0;
    text-align: center;
  }
  .identity__name {
    display: inline-block;
    font-family: "Libre Baskerville", "Baskerville", serif;
    font-size: 42px;
    font-weight: 400;
    color: var(--ink);
    letter-spacing: 1px;
    vertical-align: bottom;
  }
  .identity__role {
    display: inline-block;
    font-family: "Lato", sans-serif;
    font-weight: 300;
    font-size: 14px;
    color: var(--muted);
    letter-spacing: 1px;
    margin-left: 8px;
    vertical-align: bottom;
    padding-bottom: 22px;
  }

  .contact {
    position: absolute;
    font-family: "Libre Baskerville", "Baskerville", serif;
    font-size: 17px;
    color: var(--text);
    white-space: nowrap;
  }
  .contact::before {
    content: "";
    display: inline-block;
    width: 6px;
    height: 6px;
    border-radius: 50%;
    background: var(--ink);
    margin-right: 6px;
    vertical-align: middle;
  }
  .contact--web { top: 150px; left: 300px; }
  .contact--phone { top: 196px; left: 250px; }
  .contact--email { top: 236px; left: 28px; }

  /* back */
  .card--back .rule--top-thick { top: 10px; }
  .card--back .rule--top-thin { top: 28px; }
  .card--back .rule--bottom-thick { bottom: 26px; }
  .card--back .rule--bottom-thin { bottom: 8px; }

  .brand {
    position: absolute;
    top: 96px;
    left: 0;
    right: 0;
    text-align: center;
  }
  .brand__name {
    font-family: "Libre Baskerville", "Baskerville", serif;
    font-weight: 700;
    font-size: 50px;
    color: var(--text);
    letter-spacing: 2px;
  }
  .brand__tagline {
    margin-top: 16px;
    font-family: "Libre Baskerville", "Baskerville", serif;
    font-size: 14px;
    color: var(--text);
  }
</style>
</head>
<body>
<main class="stage">
  <section class="card card--front" aria-label="Card front">
    <div class="rule rule--thin rule--top"></div>
    <div class="identity">
      <h1 class="identity__name">Dev Lunor</h1>
      <span class="identity__role">Head Photographer</span>
    </div>
    <p class="contact contact--web">www.tamkeza.example</p>
    <p class="contact contact--phone">+65 81749026</p>
    <p class="contact contact--email">jun@tamkeza.example</p>
    <div class="rule rule--thick rule--bottom-thick"></div>
    <div class="rule rule--thin rule--bottom-thin"></div>
  </section>

  <section class="card card--back" aria-label="Card back">
    <div class="rule rule--thick rule--top-thick"></div>
    <div class="rule rule--thin rule--top-thin"></div>
    <div class="brand">
      <p class="brand__name">TamKeza</p>
      <p class="brand__tagline">Wedding and event photography company</p>
    </div>
    <div class="rule rule--thick rule--bottom-thick"></div>
    <div class="rule rule--thin rule--bottom-thin"></div>
  </section>
</main>
</body>
</html>
```